Business Card for my Photography/Video Business

I would like the card to say Event Photographer and Videographer. I like the Black and Gold look to it as well but open to other options. I don't want it to be super vibrant or colorful. Simple, elegant and professional

```html
<!DOCTYPE html>
<html lang="en">
<head>
<meta charset="UTF-8">
<title>Northlight Business Card</title>
<link rel="stylesheet" href="https://fonts.googleapis.com/css2?family=Josefin+Sans:wght@400;600&family=Montserrat:wght@400;600&display=swap">
<style>
  :root {
    --page-bg: #e9e8e8;
    --card-dark: #4a3a2c;
    --card-light: #d6d0cc;
    --gold: #d7b545;
    --gold-soft: #c9a94a;
    --brown-ink: #4f3f31;
  }
  * { margin: 0; padding: 0; box-sizing: border-box; }
  html, body {
    width: 1200px; height: 800px; overflow: hidden;
    background: var(--page-bg);
  }
  .canvas {
    width: 1200px; height: 800px;
    display: flex; align-items: center; justify-content: center; gap: 60px;
  }
  .card {
    width: 520px; height: 298px;
    border-radius: 3px;
    box-shadow: 0 10px 24px rgba(0,0,0,0.18);
    position: relative;
    display: flex; flex-direction: column; align-items: center; justify-content: center;
  }
  .card--front { background: var(--card-dark); }
  .card--back { background: var(--card-light); border: 3px solid #2e241b; }

  .brand {
    display: flex; align-items: center; gap: 14px;
  }
  .brand__dot {
    width: 58px; height: 58px; border-radius: 50%;
    flex: none;
  }
  .brand__name {
    font-family: "Josefin Sans", sans-serif;
    font-weight: 400;
    font-size: 46px;
    letter-spacing: 3px;
    line-height: 1;
    padding-top: 8px;
  }
  .card--front .brand__dot { background: var(--gold); }
  .card--front .brand__name { color: var(--gold); }
  .card--back .brand__dot { background: var(--brown-ink); width: 48px; height: 48px; }
  .card--back .brand__name { color: var(--brown-ink); font-size: 38px; }

  .website {
    font-family: "Montserrat", sans-serif;
    font-size: 12px;
    letter-spacing: 3px;
  }
  .card--front .website { color: var(--gold-soft); margin-top: 34px; }

  .contact {
    margin-top: 18px;
    display: flex; flex-direction: column; align-items: center;
    color: var(--brown-ink);
    font-family: "Montserrat", sans-serif;
  }
  .contact__name { font-weight: 600; font-size: 18px; letter-spacing: 1px; }
  .contact__title { font-weight: 600; font-size: 10px; letter-spacing: 1px; margin-top: 2px; }
  .contact__rule { width: 110px; height: 1.5px; background: var(--brown-ink); margin: 8px 0 10px; }
  .contact__row {
    display: flex; gap: 26px; font-size: 12px; align-items: center;
  }
  .contact__item { display: flex; align-items: center; gap: 6px; }
  .contact__item svg { width: 12px; height: 12px; fill: var(--brown-ink); }
  .card--back .website { color: var(--brown-ink); margin-top: 10px; font-size: 11px; }
</style>
</head>
<body>
  <main class="canvas">
    <section class="card card--front">
      <div class="brand">
        <span class="brand__dot"></span>
        <span class="brand__name">NORTHLIGHT</span>
      </div>
      <p class="website">www.yourwebsite.com</p>
    </section>

    <section class="card card--back">
      <div class="brand">
        <span class="brand__dot"></span>
        <span class="brand__name">NORTHLIGHT</span>
      </div>
      <div class="contact">
        <p class="contact__name">YOUR NAME</p>
        <p class="contact__title">JOB TITLE</p>
        <span class="contact__rule"></span>
        <div class="contact__row">
          <span class="contact__item">
            <svg viewBox="0 0 12 12" aria-hidden="true"><path d="M1 3 Q1 1 3 1 H9 Q11 1 11 3 V4 H8 V3 H4 V4 H1 Z M2 5 H10 L11 11 H1 Z"/></svg>
            000 000 0000
          </span>
          <span class="contact__item">
            <svg viewBox="0 0 12 12" aria-hidden="true"><path d="M1 2 H11 V10 H1 Z M1.5 2.5 L6 6.5 L10.5 2.5 Z" fill-rule="evenodd"/></svg>
            Youremail@xyz.com
          </span>
        </div>
        <p class="website">www.yourwebsite.com</p>
      </div>
    </section>
  </main>
</body>
</html>
```